Existing company needs Rebranding on logo and website!!

the company is called Harvest Bridge (www.harvestbridgefund.co.uk) check the site to see the existing site and logo, this has to change and must be completely different.

I want to the turn the website into a crowd funding site, but i want an inovative and interacive site. Have a look http://www.lendora.org/about/how or https://www.fundlarkly.com/ to get an idea of what is required. However i do not want my site to be anything like this. It is 2015 so web browser can do alot. when it comes to selecting project proposals on the site i want them them to pop up use your imagination your the desgner. ofcourse the site will be taking card payments and possibly bank transfers and maybe zentopay. the usual API are already on the site so you wont need to do much. the site is hosted by wordpress so i do prefer it to stay there. i am familiar with that platform.

interms of creativity you have full control we wil be working closely and i expect to be kept in the loop as things develope.

the site will also need to be turn into a mobile app which serves different purposes depending if your an investor or project sponsor.

i will give you all the information required we can communicate on chatvolt email or telephone i am flexible.

many thanks

Target Market(s)

Investors

Industry/Entity Type

Finance

Number of Pages Required

5+ page

Font styles to use
Sans Serif

Colors
3176b5
f04a50
abd036
00a990

Requirements
Must have
• i want the designer to look at my existing site www.harvestbridgefund.co.uk and come up with a better design concept.

```html
<!DOCTYPE html>
<html lang="en">
<head>
<meta charset="utf-8">
<title>Harvest Bridge – Crowdfunding for Growing Ideas</title>
<link href="https://fonts.googleapis.com/css?family=Montserrat:400,700|Open+Sans:400,600,700&display=swap" rel="stylesheet">
<style>
:root{
  --blue:#3176b5;
  --red:#f04a50;
  --green:#abd036;
  --teal:#00a990;
  --ink:#222;
  --muted:#666;
  --footer:#1f1f1f;
  --footer-bottom:#141414;
  --light:#f3f3f3;
}
*{box-sizing:border-box;margin:0;padding:0}
html,body{width:1200px;height:2959px;overflow:hidden}
body{font-family:'Open Sans',sans-serif;color:var(--ink);background:#fff;font-size:14px;line-height:1.6}
.wrap{width:980px;margin:0 auto;position:relative}
h1,h2,h3,h4{font-family:'Montserrat',sans-serif}

/* top bar */
.topbar{height:62px;background:#fff}
.topbar .wrap{display:flex;align-items:center;justify-content:space-between;height:62px}
.brand{font-family:'Montserrat',sans-serif;font-weight:700;font-size:26px;color:var(--teal);letter-spacing:-.5px}
.top-actions{display:flex;gap:10px;align-items:center}
.btn-sm{font-size:11px;font-weight:700;padding:5px 14px;border-radius:3px;text-transform:uppercase}
.btn-outline{border:1px solid var(--teal);color:var(--teal)}
.btn-fill{background:var(--teal);color:#fff}
.lang{border:1px solid #ccc;font-size:11px;padding:4px 10px;width:130px;display:flex;justify-content:space-between;color:#444;margin-left:18px}
.nav{background:var(--blue);height:39px}
.nav ul{list-style:none;display:flex;gap:30px;height:39px;align-items:center}
.nav li{color:#fff;font-size:12px;font-weight:600;text-transform:uppercase;white-space:nowrap}

/* hero */
.hero{position:relative;height:389px;overflow:hidden}
.hero-photo{position:absolute;inset:0;background:linear-gradient(90deg,#4c5a3a 0%,#7f8c6a 30%,#c9c6bb 55%,#e8e2da 75%,#b9b1a8 100%)}
.hero-shade{position:absolute;inset:0;background:rgba(0,0,0,.18)}
.hero-copy{position:relative;text-align:center;color:#fff;padding-top:142px}
.hero-copy h1{font-size:50px;font-weight:700;letter-spacing:1px;line-height:1.1}
.hero-copy p{font-family:'Montserrat',sans-serif;font-size:16px;text-transform:uppercase;margin-top:6px}
.btn{display:inline-block;background:var(--red);color:#fff;font-weight:700;font-size:15px;padding:10px 34px;border-radius:3px}
.hero-copy .btn{margin-top:44px}

/* leader band */
.leader{position:relative;height:144px}
.leader svg{position:absolute;left:0;top:0}
.leader-copy{position:relative;text-align:center;padding-top:32px}
.leader-copy h2{font-size:25px;font-weight:700}
.leader-copy h2 span{color:var(--red)}
.leader-copy p{font-size:11px;text-transform:uppercase;margin-top:2px;font-weight:600}

/* services */
.services{display:grid;grid-template-columns:repeat(4,1fr);padding-top:12px;height:245px}
.service{padding:0 28px;border-left:1px solid #ddd}
.service:first-child{border-left:0}
.service-head{display:flex;justify-content:center}
.service h3{font-size:19px;font-weight:700;text-align:center;margin:6px 0 8px}
.service p{font-size:13px;color:var(--muted);text-align:center;line-height:1.5}

/* about */
.about{position:relative;height:410px;color:#fff}
.about svg.bg{position:absolute;top:0;left:0}
.about .wrap{padding-top:52px}
.about h2{text-align:center;font-size:46px;font-weight:700}
.about-cols{display:grid;grid-template-columns:1fr 1fr;gap:40px;margin-top:18px}
.about-text{font-size:13px;text-align:right;line-height:1.75}
.checks{list-style:none}
.checks li{display:flex;gap:12px;align-items:center;font-size:15px;font-weight:600;margin-bottom:7px}
.checks svg{flex:none}
.about .btn{display:block;width:200px;margin:30px auto 0;text-align:center}

/* feature */
.feature{display:flex;height:474px;background:#fff}
.feature-photo{width:585px;background:linear-gradient(135deg,#3a3f45 0%,#8a9097 35%,#d8dde1 60%,#f1f1f1 100%)}
.feature-copy{padding:78px 0 0 28px;width:480px}
.feature-copy h2{font-size:42px;line-height:1.15;font-weight:700;color:var(--teal)}
.feature-copy h2 span{color:var(--red)}
.feature-copy p{font-size:13px;color:var(--muted);margin-top:22px;line-height:1.75}

/* testimonials */
.clients{background:var(--teal);height:480px;color:#fff;text-align:center}
.clients h2{padding-top:46px;font-size:28px;font-weight:700}
.clients .sub{font-size:11px;text-transform:uppercase;font-weight:600}
.cards{display:grid;grid-template-columns:repeat(3,1fr);gap:28px;margin-top:34px}
.card{background:#fff;color:var(--ink);height:307px}
.card-photo{height:150px;background:linear-gradient(135deg,#d9d4cb,#8f8a84)}
.card p{font-size:13px;color:var(--muted);padding:14px 24px 0;line-height:1.55}
.card h4{font-size:15px;margin-top:12px;font-weight:700}

/* partners */
.partners{background:var(--light);height:335px;text-align:center}
.partners h2{padding-top:50px;font-size:38px;font-weight:700}
.partners .sub{font-size:11px;text-transform:uppercase;font-weight:600}
.badges{display:flex;justify-content:space-between;align-items:center;margin-top:52px;padding:0 20px}
.badge{background:#c9c9c9;border-radius:4px}

/* footer */
.footer{background:var(--footer);height:300px;color:#bbb}
.footer .wrap{display:grid;grid-template-columns:330px 220px 190px 1fr;gap:10px;padding-top:40px}
.footer .brand{font-size:25px}
.footer-about{font-size:12px;text-transform:uppercase;line-height:1.8;margin-top:18px;padding-right:20px}
.footer-about.extra{margin-top:22px}
.footer h4{font-family:'Open Sans',sans-serif;font-size:13px;text-transform:uppercase;color:#fff;font-weight:600;margin-bottom:16px;padding-top:6px}
.links{list-style:none;font-size:12px;text-transform:uppercase;line-height:2}
.contact li{display:flex;gap:10px;align-items:flex-start;font-size:12px;margin-bottom:10px;list-style:none}
.social{display:flex;gap:8px}
.social span{width:36px;height:36px;display:block}
.pay-name{font-family:'Open Sans',sans-serif;font-weight:700;font-size:26px;color:#fff;margin:22px 0 8px 56px}
.cards-row{display:flex;gap:6px}
.cards-row span{width:36px;height:22px;background:#fff;border-radius:2px;display:block}
.bottom{background:var(--footer-bottom);height:95px;color:#999;font-size:11px;text-transform:uppercase}
.bottom .wrap{display:flex;justify-content:space-between;padding-top:36px}
.bottom nav{display:flex;gap:22px}
</style>
</head>
<body>

<header class="topbar">
  <div class="wrap">
    <div class="brand">Harvest Bridge</div>
    <div class="top-actions">
      <span class="btn-sm btn-outline">Sign up</span>
      <span class="btn-sm btn-fill">Login</span>
      <span class="lang"><span>English</span><span>&#9662;</span></span>
    </div>
  </div>
</header>
<nav class="nav">
  <div class="wrap">
    <ul>
      <li>Browse Projects &#9662;</li><li>How It Works</li><li>Invest</li><li>Start a Project</li><li>Sponsors &#9662;</li><li>Success Stories</li><li>Help</li>
    </ul>
  </div>
</nav>

<section class="hero">
  <div class="hero-photo" role="img" aria-label="Photo of a smiling businesswoman on the phone in a bright office with plants"></div>
  <div class="hero-shade"></div>
  <div class="hero-copy">
    <h1>FUND IDEAS THAT GROW</h1>
    <p>Back local projects and share in their harvest</p>
    <span class="btn">Enter Website</span>
  </div>
</section>

<section class="leader">
  <svg width="1200" height="144" viewBox="0 0 1200 144">
    <path d="M0 0H1200V30Q600 0 0 30Z" fill="var(--green)"/>
    <path d="M0 96Q600 130 1200 96V144H0Z" fill="var(--green)"/>
    <path d="M0 30Q600 0 1200 30V96Q600 130 0 96Z" fill="#fff"/>
  </svg>
  <div class="leader-copy">
    <h2>Crowdfunding made simple. Our investors have pledged over <span>£1,000,000</span>.</h2>
    <p>Pick a project, pledge by card, bank transfer or zentopay and follow every step of its growth</p>
  </div>
</section>

<section class="wrap services">
  <div class="service">
    <div class="service-head">
      <svg width="46" height="46" viewBox="0 0 46 46"><path d="M8 24L16 14L24 24H19V40H13V24Z" fill="var(--red)"/><path d="M22 20L31 8L40 20H34V40H28V20Z" fill="var(--red)"/></svg>
    </div>
    <h3>Investments</h3>
    <p>Back vetted proposals from as little as £25 and watch your returns grow.</p>
  </div>
  <div class="service">
    <div class="service-head">
      <svg width="46" height="46" viewBox="0 0 46 46"><path d="M23 4L40 10V22C40 32 32 39 23 42C14 39 6 32 6 22V10Z" fill="var(--blue)"/><path d="M16 23L21 28L31 17" stroke="#fff" stroke-width="3.5" fill="none"/></svg>
    </div>
    <h3>Protection</h3>
    <p>Every sponsor is checked and every pledge is held safely until funded.</p>
  </div>
  <div class="service">
    <div class="service-head">
      <svg width="46" height="46" viewBox="0 0 46 46"><ellipse cx="17" cy="34" rx="12" ry="6" fill="#e7b416"/><ellipse cx="17" cy="28" rx="12" ry="6" fill="#f3c623"/><circle cx="31" cy="18" r="12" fill="#f3c623" stroke="#e7b416" stroke-width="2"/></svg>
    </div>
    <h3>Payments</h3>
    <p>Pay by card, bank transfer or zentopay in one quick secure step.</p>
  </div>
  <div class="service">
    <div class="service-head">
      <svg width="46" height="46" viewBox="0 0 46 46"><circle cx="23" cy="14" r="9" fill="#7d3fb0"/><path d="M6 42C6 30 14 25 23 25S40 30 40 42Z" fill="#7d3fb0"/></svg>
    </div>
    <h3>Sponsors</h3>
    <p>Project sponsors get guidance to shape, launch and report on ideas.</p>
  </div>
</section>

<section class="about">
  <svg class="bg" width="1200" height="410" viewBox="0 0 1200 410"><path d="M0 30L600 0L1200 30V410H0Z" fill="var(--blue)"/></svg>
  <div class="wrap">
    <h2>About Harvest Bridge</h2>
    <div class="about-cols">
      <p class="about-text">Harvest Bridge connects investors with the people behind promising projects. Sponsors share their proposals, investors browse them in an interactive gallery and pledge in a few clicks. Each project reports progress openly, so backers always know where their money is working and what it is growing into over time.</p>
      <ul class="checks">
        <li><svg width="18" height="18" viewBox="0 0 18 18"><rect width="18" height="18" rx="2" fill="#fff"/><path d="M4 9L8 13L14 5" stroke="var(--blue)" stroke-width="2.4" fill="none"/></svg>Proposals open in a quick pop-up view.</li>
        <li><svg width="18" height="18" viewBox="0 0 18 18"><rect width="18" height="18" rx="2" fill="#fff"/><path d="M4 9L8 13L14 5" stroke="var(--blue)" stroke-width="2.4" fill="none"/></svg>Every sponsor is checked by our team.</li>
        <li><svg width="18" height="18" viewBox="0 0 18 18"><rect width="18" height="18" rx="2" fill="#fff"/><path d="M4 9L8 13L14 5" stroke="var(--blue)" stroke-width="2.4" fill="none"/></svg>Pledge by card, transfer or zentopay.</li>
        <li><svg width="18" height="18" viewBox="0 0 18 18"><rect width="18" height="18" rx="2" fill="#fff"/><path d="M4 9L8 13L14 5" stroke="var(--blue)" stroke-width="2.4" fill="none"/></svg>Live progress updates on each project.</li>
        <li><svg width="18" height="18" viewBox="0 0 18 18"><rect width="18" height="18" rx="2" fill="#fff"/><path d="M4 9L8 13L14 5" stroke="var(--blue)" stroke-width="2.4" fill="none"/></svg>Mobile app for investors and sponsors.</li>
      </ul>
    </div>
    <span class="btn">Get Update</span>
  </div>
</section>

<section class="feature">
  <div class="feature-photo" role="img" aria-label="Photo of a hand holding a smartphone beside a laptop showing the website"></div>
  <div class="feature-copy">
    <h2>Every Proposal One Click <span>Away, On Your Desk Or In Your Pocket.</span></h2>
    <p>Tap any project card and its proposal pops open with the story, the goal, the funding so far and the sponsor's plan. Compare projects side by side, save favourites and pledge without leaving the page, on the website or in the mobile app.</p>
  </div>
</section>

<section class="clients">
  <div class="wrap">
    <h2>What our clients says :)</h2>
    <p class="sub">Investors and sponsors who grew with Harvest Bridge</p>
    <div class="cards">
      <div class="card">
        <div class="card-photo" role="img" aria-label="Photo of a client working on a laptop"></div>
        <p>I found a farm project in minutes, pledged by card and now get an update every month. Simple and honest investing.</p>
        <h4>JERIN DOE</h4>
      </div>
      <div class="card">
        <div class="card-photo" role="img" aria-label="Photo of a client in a business suit"></div>
        <p>Our workshop reached its goal in six weeks. The team helped us shape the proposal so investors understood it fast.</p>
        <h4>JERIN DOE</h4>
      </div>
      <div class="card">
        <div class="card-photo" role="img" aria-label="Photo of a group of business clients"></div>
        <p>The pop-up proposals make it easy to compare projects. We now back several ideas together as a small group.</p>
        <h4>JERIN DOE</h4>
      </div>
    </div>
  </div>
</section>

<section class="partners">
  <div class="wrap">
    <h2>Our Partners</h2>
    <p class="sub">Organisations that help our projects grow</p>
    <div class="badges">
      <span class="badge" style="width:90px;height:80px"></span>
      <span class="badge" style="width:110px;height:60px"></span>
      <span class="badge" style="width:110px;height:34px"></span>
      <span class="badge" style="width:120px;height:34px"></span>
      <span class="badge" style="width:80px;height:34px"></span>
      <span class="badge" style="width:100px;height:70px"></span>
    </div>
  </div>
</section>

<footer class="footer">
  <div class="wrap">
    <div>
      <div class="brand">Harvest Bridge</div>
      <p class="footer-about">A crowdfunding platform that bridges investors and project sponsors. Browse proposals, pledge securely and follow each idea from first seed to full harvest.</p>
      <p class="footer-about extra">Grow together, invest together</p>
    </div>
    <div>
      <h4>Important Links</h4>
      <ul class="links">
        <li>Browse Projects</li><li>How It Works</li><li>Invest</li><li>Start a Project</li><li>Sponsors</li><li>Success Stories</li><li>Help</li>
      </ul>
    </div>
    <div>
      <h4>Contact Info</h4>
      <ul class="contact">
        <li><svg width="14" height="14" viewBox="0 0 14 14"><path d="M3 1L5 4L4 6Q6 9 8 10L10 9L13 11L12 13Q6 13 1 4Z" fill="#bbb"/></svg>+44 20 7946 0182</li>
        <li><svg width="14" height="14" viewBox="0 0 14 14"><path d="M3 1L5 4L4 6Q6 9 8 10L10 9L13 11L12 13Q6 13 1 4Z" fill="#bbb"/></svg>+44 20 7946 0183</li>
        <li><svg width="14" height="14" viewBox="0 0 14 14"><rect x="1" y="3" width="12" height="9" fill="none" stroke="#bbb" stroke-width="1.5"/><path d="M1 3L7 8L13 3" stroke="#bbb" stroke-width="1.5" fill="none"/></svg>info@harvestbridge.co.uk</li>
        <li><svg width="14" height="16" viewBox="0 0 14 16"><path d="M7 1C3.7 1 1.5 3.4 1.5 6.2C1.5 10 7 15 7 15S12.5 10 12.5 6.2C12.5 3.4 10.3 1 7 1Z" fill="#bbb"/><circle cx="7" cy="6" r="2" fill="var(--footer)"/></svg>42 Mercer Lane,<br>Leeds, UK</li>
      </ul>
    </div>
    <div>
      <h4>Get Connected With Us</h4>
      <div class="social">
        <span style="background:var(--blue)"></span>
        <span style="background:#3aa9e8"></span>
        <span style="background:var(--red)"></span>
      </div>
      <div class="pay-name">zentopay</div>
      <div class="cards-row"><span></span><span></span><span></span><span></span><span></span></div>
    </div>
  </div>
</footer>
<div class="bottom">
  <div class="wrap">
    <span>Copyright : Harvest Bridge . All right reserved</span>
    <nav><span>Disclaimer</span><span>|</span><span>Privacy Policy</span><span>|</span><span>Terms and Conditions</span></nav>
  </div>
</div>

</body>
</html>
```